Feng shui business card for immigration law firm

Immigration law firm would like to create the business card based and look like the Green Card (lawful permanent resident card of USA). Attached please see the sample of American Green Card. The whole business card should be performed based on the FENG SHUI style: no sharp angles. Please delete all letters and fingerprint on the sample green card and put info the following order.

Target Market(s)

Immigration clients in USA

Industry/Entity Type

Business

Contact Information for Business Card

Immigration law firm would like to create the business card based and look like the Green Card (lawful permanent resident card of USA). Attached please see the sample of American Green Card. The whole business card should be performed based on the FENG SHUI style: no sharp angles. Please delete all letters on sample green card and put info the following order:

TOLAN BERIKSOVA, ESQ.
BERIKSOVA LAW GROUP, P.A.
PRACTICE LIMITED TO IMMIGRATION LAW

4370 WEST CORVINDALE PARK BOULVERD
SUITE #218
CORVINDALE PARK, FLORIDA 33174

PHONE: 754-555-0162
EMAIL: TBERIKSOVA@QUELMAIL.EXAMPLE
WEBSITE: WWW.ZORVEL-VISAHELP.EXAMPLE

The tips for the best business card
1. It is recommended to avoid using sharp points in the logo because such logos generate negative energy. Never use sharp and pointed element like spears, knives or swords in your logo.
2. One of the most essential elements in Feng Shui good flow and space which means that there should not be any obstruction, for example, there should not be any border around the card as it stop the energy flow.
3. Keep clear of clutter – Just like applying this feng shui concept to home and office, it should also be applied to designing your name card. Always keep your card as clean and concise as possible by removing all redundant information and put only relevant ones.
4. Name should not be placed in the center of the card because it cause stress and pressure to the owner.

Font styles to use
Other font styles liked:
• Garamond or Times New Roman

Requirements
Must have
• Feng shui business card

```html
<!DOCTYPE html>
<html lang="en">
<head>
<meta charset="utf-8">
<title>Beriksova Law Group – Business Card</title>
<link href="https://fonts.googleapis.com/css2?family=EB+Garamond:wght@400;500;600&display=swap" rel="stylesheet">
<style>
  :root {
    --page-bg: #2a2d31;
    --card-white: #f7f8f4;
    --card-teal: #5fb7c4;
    --card-teal-pale: #cfe9ea;
    --band-green: #3b6e57;
    --ink: #1c1c1c;
    --seal-teal: #8ab8b3;
    --sky-blue: #1f418f;
    --flag-soft-light: #e4dfe5;
    --flag-soft-red: #c0505a;
    --gold: #d9b332;
  }
  * { margin: 0; padding: 0; box-sizing: border-box; }
  html, body { width: 1200px; height: 1200px; overflow: hidden; }
  body {
    background: var(--page-bg);
    position: relative;
    font-family: "EB Garamond", "Times New Roman", serif;
  }
  .card {
    position: absolute;
    left: 220px;
    width: 760px;
    height: 422px;
    border-radius: 32px;
    overflow: hidden;
  }
  .card-front { top: 132px; background: var(--card-white); }
  .card-back { top: 624px; background: var(--sky-blue); }

  .front-artwork {
    position: absolute; inset: 0;
    background:
      radial-gradient(ellipse 320px 260px at 640px 230px, rgba(95,183,196,.55), transparent 70%),
      linear-gradient(100deg, var(--card-white) 0%, var(--card-white) 35%, var(--card-teal-pale) 70%, #e9f1e4 100%);
  }
  .security-strip {
    position: absolute; left: 410px; top: 0; width: 350px; height: 28px;
    background: linear-gradient(90deg, #d9e3ec, #9fd3d6, #7cc3c9);
  }
  .band-name {
    position: absolute; left: 0; top: 0; width: 410px; height: 68px;
    background: var(--band-green);
  }
  .band-firm {
    position: absolute; left: 394px; top: 28px; width: 366px; height: 70px;
    background: var(--band-green);
    border-bottom-left-radius: 10px;
  }
  .attorney-name {
    position: absolute; left: 24px; top: 20px;
    color: #fff; font-size: 29px; font-weight: 500; letter-spacing: .3px;
    line-height: 1.2; white-space: nowrap;
  }
  .firm-name {
    position: absolute; left: 32px; top: 10px;
    color: #fff; font-size: 20px; line-height: 26px; white-space: nowrap;
  }
  .address {
    position: absolute; left: 58px; top: 85px;
    color: var(--ink); font-size: 21px; font-weight: 600; line-height: 26px;
    text-transform: uppercase;
  }
  .seal {
    position: absolute; left: 62px; top: 212px; width: 197px; height: 197px;
    border-radius: 50%;
    background: radial-gradient(circle at 45% 40%, #b5d6d2, var(--seal-teal) 70%, #6fa39d);
  }
  .contacts {
    position: absolute; left: 286px; top: 243px; list-style: none;
    color: var(--ink); font-size: 33px; line-height: 45px;
  }
  .contacts li { display: flex; align-items: center; gap: 10px; white-space: nowrap; }
  .contacts svg { width: 20px; height: 20px; flex: none; }

  .back-artwork {
    position: absolute; inset: 0;
    background:
      radial-gradient(ellipse 110px 130px at 20px 380px, rgba(255,255,255,.9), transparent 70%),
      var(--sky-blue);
  }
  .flag-area {
    position: absolute; left: 180px; top: 110px; width: 472px; height: 312px;
    background: linear-gradient(135deg, var(--flag-soft-light), var(--flag-soft-red));
    border-radius: 24px 24px 0 0;
  }
  .brand {
    position: absolute; left: 336px; top: 24px; display: flex; align-items: center; gap: 8px;
  }
  .brand-mark {
    width: 64px; height: 64px; border-radius: 50%; border: 3px solid var(--gold);
  }
  .brand-text {
    color: var(--gold); font-size: 23px; font-weight: 600; line-height: 20px;
    letter-spacing: 2.5px; text-align: center; white-space: nowrap;
  }
</style>
</head>
<body>

<section class="card card-front">
  <div class="front-artwork" role="img" aria-label="Pale green-card style security background with faint teal statue motif"></div>
  <div class="security-strip" role="img" aria-label="Holographic security strip"></div>
  <div class="band-name"><p class="attorney-name">TOLAN BERIKSOVA, ESQ.</p></div>
  <div class="band-firm">
    <p class="firm-name">BERIKSOVA LAW GROUP, P.A.<br>Practice Limited To Immigration Law</p>
  </div>
  <p class="address">4370 West Corvindale<br>Park Boulverd<br>Suite #218<br>Corvindale Park,<br>Florida 33174</p>
  <div class="seal" role="img" aria-label="Engraved national seal medallion"></div>
  <ul class="contacts">
    <li><svg viewBox="0 0 24 24"><path d="M7 2c1 0 2 3 2 5s-2 2-2 3 2 5 4 7 2 0 3 0 4 1 4 2-1 3-3 3C9 22 2 12 4 5c.5-2 2-3 3-3z" fill="#1c1c1c"/></svg>754-555-0162</li>
    <li><svg viewBox="0 0 24 24"><circle cx="12" cy="12" r="4" fill="none" stroke="#1c1c1c" stroke-width="2.4"/><path d="M16 8v5c0 3 4 3 4-1a8 8 0 1 0-3 6" fill="none" stroke="#1c1c1c" stroke-width="2.4" stroke-linecap="round"/></svg>tberiksova@quelmail.example</li>
    <li><svg viewBox="0 0 24 24"><g fill="none" stroke="#1c1c1c" stroke-width="1.8"><circle cx="12" cy="12" r="10"/><ellipse cx="12" cy="12" rx="4.5" ry="10"/><path d="M2 12h20M4 7h16M4 17h16"/></g></svg>www.zorvel-visahelp.example</li>
  </ul>
</section>

<section class="card card-back">
  <div class="back-artwork" role="img" aria-label="Deep blue sky with a soft cloud"></div>
  <div class="flag-area" role="img" aria-label="Photo of a waving national flag on a pole"></div>
  <div class="brand">
    <span class="brand-mark"></span>
    <p class="brand-text">TOLAN BERIKSOVA<br>ATTORNEY AT LAW.</p>
  </div>
</section>

</body>
</html>
```